Borin's Yard

I need a Bussiness Card for my new company in Miami Beach, my company is based in Winwood Miami and all around me is arts soo I would like my card with stripes, art design.

Target Market(s)

Artists, Actress, actors, show bussiness

Industry/Entity Type

It Company

Requirements
Must have
• Art Design

```html
<!DOCTYPE html>
<html lang="en">
<head>
<meta charset="utf-8">
<title>Borin's Yard – Business Card</title>
<link rel="stylesheet" href="https://fonts.googleapis.com/css2?family=Open+Sans:wght@400;700&display=swap">
<style>
  :root {
    --bg: #e9e7e4;
    --card-white: #ffffff;
    --brand-red: #c0282f;
    --brand-red-dark: #8c1c24;
    --brand-red-light: #d9444b;
    --brand-gold: #f2b81c;
    --ink-on-red: #ffffff;
    --card-shadow: rgba(0, 0, 0, 0.18);
  }
  * { box-sizing: border-box; margin: 0; padding: 0; }
  html, body {
    width: 1200px; height: 901px; overflow: hidden;
    background: var(--bg);
    font-family: "Open Sans", Arial, sans-serif;
  }
  .canvas {
    position: relative; width: 1200px; height: 901px;
    display: flex; justify-content: center; align-items: center; gap: 80px;
  }
  .card {
    position: relative; width: 340px; height: 580px;
    border-radius: 30px; overflow: hidden;
    background: var(--card-white);
    box-shadow: 0 8px 24px var(--card-shadow);
  }
  .card-waves { position: absolute; inset: 0; width: 100%; height: 100%; }
  .brand {
    position: absolute; display: flex; align-items: center; gap: 10px;
  }
  .brand-dot {
    width: 30px; height: 30px; border-radius: 50%;
    background: var(--brand-gold); flex: none;
  }
  .brand-name {
    font-weight: 700; font-size: 28px; line-height: 1;
    color: var(--brand-red); white-space: nowrap;
  }
  .card-front .brand { left: 34px; top: 48px; }
  .card-back .brand { left: 50%; top: 50%; transform: translate(-50%, -50%); }

  .person { position: absolute; left: 40px; top: 330px; color: var(--ink-on-red); }
  .person-name { font-weight: 700; font-size: 21px; letter-spacing: 0.5px; text-transform: uppercase; }
  .person-role { font-size: 14px; margin-top: 4px; padding-left: 14px; }

  .contacts {
    position: absolute; left: 40px; top: 448px; list-style: none;
    color: var(--ink-on-red); font-size: 14px;
  }
  .contacts li { display: flex; align-items: center; gap: 10px; height: 26px; }
  .contacts svg { width: 15px; height: 15px; flex: none; }
</style>
</head>
<body>
<main class="canvas">
  <!-- Front of card -->
  <section class="card card-front">
    <svg class="card-waves" viewBox="0 0 340 580" preserveAspectRatio="none" aria-hidden="true">
      <path d="M0,200 C110,160 240,150 340,190 L340,580 L0,580 Z" fill="var(--brand-red-light)"/>
      <path d="M0,214 C110,176 240,168 340,200 L340,580 L0,580 Z" fill="var(--card-white)"/>
      <path d="M0,222 C110,186 240,178 340,206 L340,580 L0,580 Z" fill="var(--brand-red-dark)"/>
      <path d="M0,262 C120,222 250,208 340,212 L340,580 L0,580 Z" fill="var(--brand-red)"/>
    </svg>
    <div class="brand">
      <span class="brand-dot"></span>
      <span class="brand-name">Borin's Yard</span>
    </div>
    <div class="person">
      <h1 class="person-name">Marcus Delane</h1>
      <p class="person-role">Managing Director</p>
    </div>
    <ul class="contacts">
      <li>
        <svg viewBox="0 0 16 16"><path d="M4 1.5l2 3-1.2 1.4c.8 1.8 2.3 3.3 4.1 4.1L10.3 8.8l3 2-0.9 2.7C7 13.4 2.6 9 2.5 3.6z" fill="#fff"/></svg>
        <span>012 555 0148</span>
      </li>
      <li>
        <svg viewBox="0 0 16 16"><rect x="1" y="3" width="14" height="10" rx="1" fill="#fff"/><path d="M1.5 3.5L8 9l6.5-5.5" stroke="var(--brand-red)" stroke-width="1.3" fill="none"/></svg>
        <span>hello@borinsyard.com</span>
      </li>
      <li>
        <svg viewBox="0 0 16 16" fill="none" stroke="#fff" stroke-width="1.3"><circle cx="8" cy="8" r="6.5"/><ellipse cx="8" cy="8" rx="3" ry="6.5"/><path d="M1.5 8h13"/></svg>
        <span>www.borinsyard.com</span>
      </li>
    </ul>
  </section>

  <!-- Back of card -->
  <section class="card card-back">
    <div class="brand">
      <span class="brand-dot"></span>
      <span class="brand-name">Borin's Yard</span>
    </div>
  </section>
</main>
</body>
</html>
```